New Innovative Counselling and psychotherapy Service needs Business Card design

Keep it simple and professional. On one side, just company name and logo (perhaps in all blue) and maybe a tag line.

On other side (all white) my name and Qualifications in centre

Industry/Entity Type

Health And Wellness

Contact Information for Business Card

Derek Hollis
Counsellor & Psychotherapist
BSc (Psychol.), BA, Dip. (Couns. & Psych.), PG.Cert (CBT), MGVrA, NWTF

I will also require Mobile no, Email and web site address of which I'll pass on to final designer.

Font styles to use
Sans Serif

Requirements
Must have
• My Logo Only and please use the colours in logo that is in it.
Should not have
• Any other images

```html
<!DOCTYPE html>
<html lang="en">
<head>
<meta charset="utf-8">
<title>Brightwell Path – Business Card</title>
<link href="https://fonts.googleapis.com/css2?family=Roboto:wght@300;400;700;900&display=swap" rel="stylesheet">
<style>
  :root {
    --backdrop: #3a3a3a;
    --card: #1f1f21;
    --card-edge: #2a2a2c;
    --blue: #3fb0ec;
    --green: #7ccd3e;
    --ink: #111111;
    --white: #ffffff;
    --emboss: #4a4a4e;
  }
  * { margin: 0; padding: 0; box-sizing: border-box; }
  html, body { width: 799px; height: 1200px; overflow: hidden; }
  body {
    background: var(--backdrop);
    font-family: "Roboto", Arial, sans-serif;
    position: relative;
  }
  .card {
    position: absolute;
    left: 100px;
    width: 600px;
    height: 350px;
    border-radius: 26px;
    background: var(--card);
    overflow: hidden;
    box-shadow: 0 14px 30px rgba(0,0,0,0.45);
  }
  .card--front { top: 140px; }
  .card--back { top: 720px; }

  /* front */
  .front-mark {
    position: absolute;
    inset: 0;
    display: flex;
    align-items: center;
    justify-content: center;
    gap: 16px;
  }
  .front-mark__dot {
    width: 54px; height: 54px; border-radius: 50%;
    background: var(--emboss);
  }
  .front-mark__name {
    font-weight: 300;
    font-size: 38px;
    color: var(--emboss);
    letter-spacing: 0.5px;
  }

  /* back */
  .info-panel {
    position: absolute;
    right: 0; top: 0;
    width: 290px; height: 200px;
    background: var(--blue);
  }
  .info-rule {
    position: absolute;
    right: 0; top: 208px;
    width: 290px; height: 5px;
    background: var(--green);
  }
  .brand {
    position: absolute;
    left: 34px; top: 110px;
  }
  .brand__dot {
    width: 112px; height: 112px; border-radius: 50%;
    background: var(--blue);
    margin-left: 70px;
    margin-bottom: 14px;
  }
  .brand__name {
    font-weight: 300;
    font-size: 34px;
    color: var(--white);
    white-space: nowrap;
  }
  .holder {
    position: absolute;
    right: 30px; top: 74px;
    text-align: right;
    color: var(--ink);
  }
  .holder__name { font-weight: 900; font-size: 25px; margin-bottom: 3px; }
  .holder__role, .holder__quals { font-weight: 700; font-size: 12.5px; line-height: 1.25; }
  .contact {
    position: absolute;
    right: 30px; bottom: 30px;
    list-style: none;
    color: var(--white);
    font-size: 16px;
    text-align: right;
  }
  .contact li { display: flex; align-items: center; justify-content: flex-end; gap: 8px; line-height: 1.5; }
  .contact svg { width: 16px; height: 16px; }
</style>
</head>
<body>

<section class="card card--front" aria-label="Card front">
  <div class="front-mark">
    <span class="front-mark__dot"></span>
    <span class="front-mark__name">Brightwell Path</span>
  </div>
</section>

<section class="card card--back" aria-label="Card back">
  <div class="info-panel"></div>
  <div class="info-rule"></div>

  <div class="brand">
    <div class="brand__dot"></div>
    <div class="brand__name">Brightwell Path</div>
  </div>

  <div class="holder">
    <div class="holder__name">Derek Hollis</div>
    <div class="holder__role">Counsellor &amp; Psychotherapist</div>
    <div class="holder__quals">BSc (Psychol.), BA, Dip. (Couns.<br>&amp; Psych.), PG.Cert (CBT),<br>MGVrA, NWTF</div>
  </div>

  <ul class="contact">
    <li>0123 456 7891
      <svg viewBox="0 0 16 16"><rect width="16" height="16" rx="2" fill="var(--card-edge)"/><path d="M4 3h3l1 3-2 1c1 2 2 3 3 3l1-2 3 1v3c-6 0-9-4-9-9z" fill="var(--blue)"/></svg>
    </li>
    <li>derek.h@BrightwellPath.com
      <svg viewBox="0 0 16 16"><rect width="16" height="16" rx="2" fill="var(--card-edge)"/><rect x="2" y="4" width="12" height="8" fill="var(--green)"/><path d="M2 4l6 5 6-5" stroke="var(--card)" stroke-width="1.2" fill="none"/></svg>
    </li>
    <li>www.BrightwellPath.com
      <svg viewBox="0 0 16 16"><rect width="16" height="16" rx="2" fill="var(--card-edge)"/><circle cx="8" cy="8" r="5.5" fill="var(--blue)"/><path d="M2.5 8h11M8 2.5c-2.5 3-2.5 8 0 11M8 2.5c2.5 3 2.5 8 0 11" stroke="var(--card)" stroke-width="0.8" fill="none"/></svg>
    </li>
  </ul>
</section>

</body>
</html>
```